Local fast-growing company in the service sector

We are looking for a modern business card design, which should also appear on our letterheads

Target Market(s)

Private and industrial sectors

Contact Information for Business Card

Vorname Name
Lindkofer Str. 18
71468 Kernfeld
Tel.: 07163-418259-0
Name@kovaltec-pbz.de

Colors
9d9d9d
919191
aaaaaa

Requirements
Must have
• The logo (file) in silver

```html
<!DOCTYPE html>
<html lang="de">
<head>
<meta charset="utf-8">
<title>KOVALTEC Visitenkarte</title>
<link href="https://fonts.googleapis.com/css2?family=Roboto:wght@400;500&display=swap" rel="stylesheet">
<style>
  :root {
    --bg: #e6e4e1;
    --frame: #919191;
    --fold: #7a7a7a;
    --paper: #f2efeb;
    --silver: #9d9d9d;
    --muted: #aaaaaa;
    --ink: #1d1d1d;
    --rule: #3a3a3a;
  }
  html, body {
    margin: 0;
    width: 1200px;
    height: 1200px;
    overflow: hidden;
    background: var(--bg);
    font-family: "Roboto", Arial, sans-serif;
  }
  .card {
    position: absolute;
    left: 100px;
    top: 300px;
    width: 1000px;
    height: 600px;
    background: var(--frame);
    box-shadow: 0 6px 18px rgba(0,0,0,0.18);
  }
  .card__panel {
    position: absolute;
    inset: 34px;
    background: var(--paper);
  }
  .card__folds {
    position: absolute;
    inset: 0;
  }
  .brand {
    position: absolute;
    left: 120px;
    top: 150px;
    display: flex;
    align-items: center;
    gap: 18px;
  }
  .brand__square {
    width: 54px;
    height: 54px;
    background: var(--silver);
  }
  .brand__name {
    font-size: 62px;
    font-weight: 500;
    color: var(--silver);
    letter-spacing: 1px;
  }
  .rule {
    position: absolute;
    right: 34px;
    height: 1.5px;
    background: var(--rule);
  }
  .rule--role { top: 272px; left: 780px; }
  .rule--name { top: 345px; left: 470px; }
  .rule--address { top: 412px; left: 470px; }
  .contact {
    position: absolute;
    color: var(--ink);
    white-space: nowrap;
  }
  .contact__role {
    left: 792px;
    top: 240px;
    font-size: 22px;
    color: var(--muted);
  }
  .contact__name {
    left: 480px;
    top: 283px;
    font-size: 44px;
  }
  .contact__address { left: 480px; top: 362px; font-size: 25px; }
  .contact__phone   { left: 480px; top: 428px; font-size: 25px; }
  .contact__email   { left: 480px; top: 470px; font-size: 25px; color: var(--muted); }
  .contact__web     { right: 70px; top: 420px; font-size: 23px; }
</style>
</head>
<body>
  <div class="card">
    <div class="card__panel"></div>
    <svg class="card__folds" width="1000" height="600" viewBox="0 0 1000 600" aria-hidden="true">
      <polygon points="966,34 966,120 900,34" fill="var(--fold)"/>
      <polygon points="966,566 966,470 880,566" fill="var(--fold)"/>
      <polygon points="34,34 34,110 100,34" fill="var(--fold)"/>
      <polygon points="34,566 34,500 110,566" fill="var(--fold)"/>
    </svg>

    <div class="brand">
      <div class="brand__square"></div>
      <div class="brand__name">KOVALTEC</div>
    </div>

    <div class="contact contact__role">| Position</div>
    <div class="rule rule--role"></div>
    <div class="contact contact__name">Vorname Name</div>
    <div class="rule rule--name"></div>
    <div class="contact contact__address">Lindkofer Str. 18, 71468 Kernfeld</div>
    <div class="rule rule--address"></div>
    <div class="contact contact__phone">Phone 07163-418259-0</div>
    <div class="contact contact__email">Name@kovaltec-pbz.de</div>
    <div class="contact contact__web">kovaltec-pbz.de</div>
  </div>
</body>
</html>
```